New Look Driving School Project

Current website:
www. pelmarsteeracademy.com

Websites that we like (use content and courses from here as well):
https://www. quorbeltlessons.com

We are looking for a fresh looking driving school website that is easy for students to find the course they are looking for, the price, and allow them to book a lesson all on our website. We would like for this website to have multiple pages: Home, Teen Courses, Adult Courses, About Us, Contact, FAQ, Blog, Requirements.

Target Market(s)

Students in High School or Parents

Industry/Entity Type

Education

Coding

Coded - Design and coding required

Number of Pages Required

5+ page

Font styles to use
Serif
Sans Serif

Colors

Designer to choose colors to be used in the design.

Requirements
Must have
• Must have a form submission and payment processing option. Must have the ability to pick a course, see available times, and process their payment online. MUST BE MOBILE FRIENDLY DESIGN.
Nice to have
• Nice to have a clean format, with big bold fonts.
Should not have
• Should not have a lot of sliders or animations. Should be very fast loading on mobile. Keep it simple but easy to read and elegant.

```html
<!DOCTYPE html>
<html lang="en">
<head>
<meta charset="utf-8">
<title>Pelmar Steer Academy</title>
<link rel="stylesheet" href="https://fonts.googleapis.com/css2?family=Ubuntu:wght@400;500;700&family=Arimo:wght@400&display=swap">
<style>
:root{
  --red:#ee1c1c;
  --red-box:#d42a30;
  --dark:#2b2f35;
  --panel:rgba(40,52,70,.78);
  --white:#fff;
  --grey-head:#efefef;
  --field:#f2f2f2;
  --field-border:#e2e2e2;
  --muted:#8a8f96;
  --title:#5a6068;
  --submit:#c4c4c4;
}
*{box-sizing:border-box;margin:0;padding:0}
html,body{width:1200px;height:517px;overflow:hidden;background:var(--white);font-family:'Ubuntu',sans-serif}
.topbar{position:absolute;left:0;top:0;width:1200px;height:32px;background:var(--red);color:var(--white);font-size:11.5px;display:flex;align-items:center}
.topbar .links{position:absolute;left:152px;display:flex;gap:5px}
.topbar .info{position:absolute;left:410px;display:flex;gap:20px;align-items:center}
.topbar .info span{display:flex;align-items:center;gap:8px}
.topbar svg{width:10px;height:10px;fill:var(--white)}
.header{position:absolute;left:0;top:32px;width:1200px;height:70px;background:var(--white)}
.brand{position:absolute;left:148px;top:28px;font-size:25px;font-weight:700;color:var(--red);letter-spacing:.6px}
.hero{position:absolute;left:0;top:102px;width:1200px;height:415px;background:linear-gradient(180deg,#2f5a9c 0%,#3f78b8 35%,#6aa3d5 70%,#b9d6ea 100%)}
.title-box{position:absolute;left:160px;top:79px;width:291px;height:47px;background:var(--red-box);color:var(--white);font-size:19px;font-weight:700;padding-left:16px;line-height:47px;letter-spacing:.4px}
.arrow-box{position:absolute;left:451px;top:79px;width:50px;height:47px;background:var(--dark);display:flex;align-items:center;justify-content:center}
.tagline{position:absolute;left:160px;top:134px;width:372px;height:71px;background:var(--panel);color:var(--white);font-size:13.5px;line-height:20px;padding:15px 16px}
.btn{position:absolute;top:229px;height:33px;border:2px solid var(--white);color:var(--white);font-family:'Arimo',sans-serif;font-size:11.5px;display:flex;align-items:center;justify-content:center;background:rgba(255,255,255,.08)}
.btn-book{left:160px;width:137px}
.btn-price{left:326px;width:148px}
.course-finder{position:absolute;left:754px;top:142px;width:273px;height:322px;background:var(--white);border-radius:2px}
.finder-head{height:45px;background:var(--grey-head);display:flex;align-items:center;justify-content:space-between;padding:0 12px}
.finder-head h2{font-size:15.5px;font-weight:700;color:var(--title)}
.field{position:absolute;height:31px;background:var(--field);border:1px solid var(--field-border);color:var(--muted);font-size:10.5px;display:flex;align-items:center;gap:7px;padding-left:8px}
.field svg{width:10px;height:10px;fill:#6e737a;flex:none}
.full{left:15px;width:242px}
.half-l{left:15px;width:117px}
.half-r{left:140px;width:117px}
.caret{position:absolute;right:8px;width:0;height:0;border-left:3.5px solid transparent;border-right:3.5px solid transparent;border-top:4px solid #6e737a}
.submit{position:absolute;left:17px;top:259px;width:238px;height:30px;background:var(--submit);color:var(--white);font-family:'Arimo',sans-serif;font-size:11px;display:flex;align-items:center;justify-content:center}
</style>
</head>
<body>
<div class="topbar">
  <div class="links"><span>About</span><span>-</span><span>Blog</span><span>-</span><span>FAQ</span><span>-</span><span>Social</span></div>
  <div class="info">
    <span><svg viewBox="0 0 10 10"><circle cx="5" cy="5" r="4" fill="none" stroke="#fff" stroke-width="1.4"/><path d="M5 2.5V5h2" stroke="#fff" stroke-width="1.2" fill="none"/></svg>Opening Hours: Mon-Fri : 9am -7pm</span>
    <span><svg viewBox="0 0 10 10"><path d="M2 0.5l2 2.2-1 1.2c.6 1.3 1.6 2.3 2.9 2.9l1.2-1 2.2 2-1.2 1.7C4.3 9.3.7 5.7.3 1.7z"/></svg>Call Us : + 555-010-4827</span>
    <span><svg viewBox="0 0 10 10"><rect x="0" y="1.5" width="10" height="7" rx="1"/><path d="M0.5 2l4.5 3.5L9.5 2" stroke="#ee1c1c" fill="none" stroke-width="1"/></svg>support@pelmarsteeracademy.com</span>
  </div>
</div>
<div class="header"><div class="brand">PELMAR STEER ACADEMY</div></div>
<div class="hero" role="img" aria-label="Blue sky with wind turbines over a sandy field">
  <div class="title-box">PELMAR STEER ACADEMY</div>
  <div class="arrow-box"><svg width="20" height="10" viewBox="0 0 20 10"><path d="M0 5h17M12 1l5 4-5 4" stroke="#fff" stroke-width="2.2" fill="none"/></svg></div>
  <div class="tagline">Experienced Instructors and Well Maintained Cars/Vehicles.</div>
  <div class="btn btn-book">BOOK LESSON</div>
  <div class="btn btn-price">COURSES PRICE</div>
</div>
<form class="course-finder">
  <div class="finder-head"><h2>Find Driving Course</h2><svg width="14" height="11" viewBox="0 0 14 11"><path d="M4 0h6l4 11H9.5L9 8H5l-.5 3H0z" fill="#5a6068"/><rect x="6.4" y="1" width="1.2" height="2.5" fill="#fff"/><rect x="6.4" y="4.5" width="1.2" height="2.5" fill="#fff"/></svg></div>
  <div class="field full" style="top:62px"><svg viewBox="0 0 10 10"><circle cx="5" cy="2.8" r="2.4"/><path d="M0.5 10c0-3 2-4.5 4.5-4.5S9.5 7 9.5 10z"/></svg>YOUR NAME</div>
  <div class="field full" style="top:101px"><svg viewBox="0 0 10 10"><rect x="0" y="1.5" width="10" height="7" rx="1"/></svg>YOUR EMAIL</div>
  <div class="field full" style="top:140px"><svg viewBox="0 0 10 10"><path d="M2 0.5l2 2.2-1 1.2c.6 1.3 1.6 2.3 2.9 2.9l1.2-1 2.2 2-1.2 1.7C4.3 9.3.7 5.7.3 1.7z"/></svg>YOUR PHONE</div>
  <div class="field half-l" style="top:179px"><svg viewBox="0 0 10 10"><rect x="0.5" y="1.5" width="9" height="8" fill="none" stroke="#6e737a"/><rect x="0.5" y="1.5" width="9" height="2"/></svg>MM/DD/Y</div>
  <div class="field half-r" style="top:179px"><svg viewBox="0 0 10 10"><path d="M1.5 0.5h5l2 2v7h-7z" fill="none" stroke="#6e737a"/><path d="M3 5h4M3 7h4" stroke="#6e737a"/></svg>COURSE TYPE<span class="caret"></span></div>
  <div class="field half-l" style="top:218px"><svg viewBox="0 0 10 10"><path d="M1 5l1.3-3h5.4L9 5v3H1z"/><circle cx="2.8" cy="8.5" r="1.2"/><circle cx="7.2" cy="8.5" r="1.2"/></svg>CAR TYPE 1<span class="caret"></span></div>
  <div class="field half-r" style="top:218px"><svg viewBox="0 0 10 10"><circle cx="5" cy="5" r="4" fill="none" stroke="#6e737a" stroke-width="1.4"/><path d="M5 2.5V5h2" stroke="#6e737a" stroke-width="1.2" fill="none"/></svg>MORNING BATC<span class="caret"></span></div>
  <div class="submit">SUBMIT ENQUIRY</div>
</form>
</body>
</html>
```